Wren Resins Needs a Box Design for their Moldable Plastic Variety Pack*

We need a design for the box that will hold the products for our variety pack. We sell moldable plastics that melt in hot water and can be shaped by hand (wrenresins.example). The products in the box will be moldable plastic pellets, sheets, strips and colors.
Boxqubo is making a digitally printed box and have supplied the dieline for you to fill in. See the attached dieline and the requirements from Boxquboo. We want the design to be bright and fun. It must incorporate our logo parrot and describe the product. A photoshop file of the parrot is attached and a file containing a simple design is attached also. The parrot can be any color. The image and wording should be on top of the box. The sides of the box don't need any words but should be designed too - we don't want white showing on the box unless it is part of the design.

Target Market(s)

Arts and crafts market. Men and women, all ages.

Industry/Entity Type

Plastic

Colors

Designer to choose colors to be used in the design.

Requirements
Must have
• Top of box must have logo parrot, wren resins name, words Moldable Plastics Variety Pack, wrenresins.example. Design must pop off the page. The font in the "Wren Resins' name should not be changed dramatically. Add a small TM symbol whenever the name Wren Resins is used.

```html
<!DOCTYPE html>
<html lang="en">
<head>
<meta charset="utf-8">
<title>Wren Resins – Moldable Plastics Variety Pack box</title>
<link rel="stylesheet" href="https://fonts.googleapis.com/css2?family=Alegreya:wght@400&family=Bebas+Neue&display=swap">
<style>
  :root {
    --ink: #202020;
    --red: #c93a35;
    --yellow: #e8cc5a;
    --teal: #3e7b8f;
    --paper: #ffffff;
    --cut: #d6eaf0;
    --slot: #3a3a3a;
    --artwork-dark: #a9783f;
    --artwork-light: #d9b46a;
  }
  html, body {
    margin: 0;
    padding: 0;
    width: 1200px;
    height: 1104px;
    overflow: hidden;
    background: var(--paper);
  }
  .dieline {
    display: block;
    width: 1200px;
    height: 1104px;
  }
  .cut-edge { fill: var(--paper); stroke: var(--cut); stroke-width: 1.2; }
  .fold-gap { stroke: var(--paper); stroke-width: 3; }
  .fill-ink { fill: var(--ink); }
  .fill-red { fill: var(--red); }
  .fill-yellow { fill: var(--yellow); }
  .fill-teal { fill: var(--teal); }
  .tuck-slot { fill: none; stroke: var(--slot); stroke-width: 1; }
  .side-copy {
    font-family: "Alegreya", Georgia, serif;
    fill: var(--paper);
    text-anchor: middle;
    font-size: 10.5px;
  }
  .side-heading {
    font-family: "Alegreya", Georgia, serif;
    fill: var(--paper);
    text-anchor: middle;
    font-size: 15px;
    letter-spacing: 0.3px;
  }
  .icon-white { fill: var(--paper); }
  .icon-ink { fill: var(--ink); }
  .brand-name {
    font-family: "Alegreya", Georgia, serif;
    fill: var(--paper);
    text-anchor: middle;
    font-size: 38px;
  }
  .product-title {
    font-family: "Bebas Neue", Impact, sans-serif;
    fill: var(--paper);
    text-anchor: middle;
    font-size: 39px;
    letter-spacing: 0.5px;
  }
  .top-url {
    font-family: "Bebas Neue", Impact, sans-serif;
    fill: var(--paper);
    text-anchor: middle;
    font-size: 20px;
    letter-spacing: 0.5px;
  }
  .rule { stroke: var(--paper); stroke-width: 2; }
</style>
</head>
<body>
<svg class="dieline" viewBox="0 0 1080 993.6" preserveAspectRatio="none" xmlns="http://www.w3.org/2000/svg">
  <defs>
    <linearGradient id="artwork-tones" x1="0" y1="0" x2="1" y2="1">
      <stop offset="0" stop-color="var(--artwork-dark)"/>
      <stop offset="0.6" stop-color="var(--artwork-light)"/>
      <stop offset="1" stop-color="var(--yellow)"/>
    </linearGradient>
  </defs>

  <!-- Side panel piece -->
  <g class="side-piece">
    <path class="cut-edge" d="M20 215 Q20 150 85 150 L470 150 Q484 150 484 165 L484 870 Q484 886 470 886 L85 886 Q20 886 20 820 Z"/>
    <path class="fill-yellow" d="M22 220 L22 205 Q22 158 82 157 L90 157 L90 220 Z"/>
    <rect class="fill-red" x="22" y="220" width="68" height="592"/>
    <path class="fill-teal" d="M22 812 L90 812 L90 870 Q40 868 22 830 Z"/>
    <path class="fill-teal" d="M92 231 L92 172 Q92 160 110 160 L458 160 Q472 160 472 180 L472 190 Q470 215 484 222 L484 231 Z"/>
    <rect class="fill-ink" x="91" y="231" width="393" height="571"/>
    <path class="fill-yellow" d="M92 802 L484 802 L484 812 Q470 820 472 845 L472 855 Q472 870 455 870 L110 870 Q92 870 92 858 Z"/>

    <g class="playing-block">
      <g class="thumb-icon" transform="translate(229 265)">
        <path class="icon-white" d="M0 6 h4 v9 h-4 z M5 6 l4 -6 q2 0 2 2 l-1 4 h5 q2 0 2 2 l-2 7 q-1 1 -2 1 h-8 z"/>
      </g>
      <text class="side-heading" x="284" y="279">PLAYING</text>
      <g class="thumb-icon" transform="translate(321 265)">
        <path class="icon-white" d="M0 6 h4 v9 h-4 z M5 6 l4 -6 q2 0 2 2 l-1 4 h5 q2 0 2 2 l-2 7 q-1 1 -2 1 h-8 z"/>
      </g>
      <text class="side-copy" x="284" y="315">Easy to Use</text>
      <text class="side-copy" x="284" y="344">Mold by Hand</text>
      <text class="side-copy" x="284" y="373">Strong &amp; Durable</text>
      <text class="side-copy" x="284" y="402">Re-melt &amp; Re-Mold</text>
      <text class="side-copy" x="284" y="431">Crafts, Repairs, Models,</text>
      <text class="side-copy" x="284" y="444">and more…</text>
      <text class="side-copy" x="284" y="473">www.wrenresins.example</text>
    </g>

    <g class="warning-block">
      <g transform="translate(219 532)">
        <path class="icon-white" d="M9 0 L18 16 L0 16 Z"/>
        <rect class="icon-ink" x="8" y="5" width="2" height="6"/>
        <rect class="icon-ink" x="8" y="12.5" width="2" height="2"/>
      </g>
      <text class="side-heading" x="284" y="546">WARNING</text>
      <g transform="translate(330 532)">
        <path class="icon-white" d="M9 0 L18 16 L0 16 Z"/>
        <rect class="icon-ink" x="8" y="5" width="2" height="6"/>
        <rect class="icon-ink" x="8" y="12.5" width="2" height="2"/>
      </g>
      <text class="side-copy" x="284" y="587">Take care to avoid burns</text>
      <text class="side-copy" x="284" y="620">Choke hazard for</text>
      <text class="side-copy" x="284" y="635">children under 3</text>
      <text class="side-copy" x="284" y="668">Supervise children</text>
      <text class="side-copy" x="284" y="683">under 7</text>
      <text class="side-copy" x="284" y="715">Not for internal use</text>
      <text class="side-copy" x="284" y="748">Keep finished product</text>
      <text class="side-copy" x="284" y="763">from extreme heat</text>
    </g>
  </g>

  <!-- Main lid piece -->
  <g class="lid-piece">
    <path class="fill-teal" d="M484 66 Q484 62 490 62 L542 62 Q545 100 552 140 L552 220 L484 220 Z"/>
    <rect class="fill-yellow" x="484" y="220" width="68" height="595"/>
    <path class="fill-teal" d="M484 815 L552 815 L552 890 Q545 930 542 970 L490 970 Q484 970 484 964 Z"/>

    <rect class="fill-yellow" x="552" y="66" width="393" height="82"/>
    <rect class="fill-red" x="552" y="148" width="393" height="70"/>
    <rect class="fill-ink" x="552" y="218" width="393" height="597"/>
    <rect class="fill-red" x="552" y="815" width="393" height="70"/>
    <rect class="fill-teal" x="552" y="885" width="393" height="80"/>

    <path class="fill-yellow" d="M945 66 L1008 66 Q1013 66 1013 71 L1013 225 L945 225 Z"/>
    <rect class="fill-teal" x="945" y="225" width="68" height="583"/>
    <path class="fill-yellow" d="M945 808 L1008 808 Q1013 808 1013 813 L1013 960 Q1013 965 1008 965 L945 965 Z"/>

    <line class="fold-gap" x1="946" y1="62" x2="946" y2="218"/>
    <line class="fold-gap" x1="946" y1="815" x2="946" y2="970"/>
    <line class="fold-gap" x1="551" y1="62" x2="551" y2="218"/>
    <line class="fold-gap" x1="551" y1="815" x2="551" y2="970"/>

    <rect class="tuck-slot" x="632" y="213" width="78" height="12" rx="5"/>
    <rect class="tuck-slot" x="787" y="213" width="78" height="12" rx="5"/>
    <rect class="tuck-slot" x="632" y="803" width="78" height="12" rx="5"/>
    <rect class="tuck-slot" x="787" y="803" width="78" height="12" rx="5"/>

    <text class="brand-name" x="750" y="318">Wren Resins</text>

    <rect class="mascot-artwork" x="622" y="362" width="258" height="190" rx="40"
          fill="url(#artwork-tones)" role="img"
          aria-label="Brand mascot illustration"/>

    <text class="product-title" x="750" y="628">MOLDABLE PLASTICS</text>
    <text class="product-title" x="750" y="668">VARIETY PACK</text>
    <line class="rule" x1="731" y1="697" x2="769" y2="697"/>
    <text class="top-url" x="750" y="750">WWW.WRENRESINS.EXAMPLE</text>
  </g>
</svg>
</body>
</html>
```